Brightwell Holdings -Business Card Design Project

I have a new logo to put onto business cards - attached
The word doc shows how I want it all laid out - front page and rear
The lettering I want is clean and rounded - modern
Updates
Project Deadline Extended
Reason: There was no original deadline!
Target Market(s)
25-49 year old leaders and entrepreneurs in Australia
Industry/Entity Type
Business

```html
<!DOCTYPE html>
<html lang="en">
<head>
<meta charset="utf-8">
<title>Brightwell Holdings – Business Card</title>
<link rel="stylesheet" href="https://fonts.googleapis.com/css2?family=Jura:wght@500;600&display=swap">
<style>
  :root {
    --page-bg: #e4e4e2;
    --card-top: #ffffff;
    --card-bottom: #ececec;
    --brand-blue: #1a5fb0;
    --swoosh-grey: #bcbcbc;
    --text-grey: #4a4a4a;
    --muted-grey: #8a8a8a;
    --rule-grey: #b5b5b5;
    --icon-grey: #5a6470;
  }
  * { box-sizing: border-box; margin: 0; padding: 0; }
  html, body {
    width: 1200px; height: 900px; overflow: hidden;
    background: var(--page-bg);
    font-family: "Jura", "Trebuchet MS", sans-serif;
  }
  .business-card {
    position: absolute; left: 100px; top: 164px;
    width: 1000px; height: 572px;
    border-radius: 44px; overflow: hidden;
    background: linear-gradient(160deg, var(--card-top) 0%, var(--card-bottom) 100%);
    box-shadow: 0 18px 40px rgba(0,0,0,0.18);
  }
  .card-swoosh { position: absolute; inset: 0; }
  .swoosh-blue { fill: var(--brand-blue); }
  .swoosh-grey { fill: var(--swoosh-grey); }

  .brand-block { position: absolute; left: 262px; top: 112px; }
  .brand-mark {
    position: absolute; left: 0; top: 6px;
    width: 64px; height: 64px; background: var(--brand-blue);
  }
  .brand-name {
    position: absolute; left: 86px; top: 0;
    white-space: nowrap;
    font-size: 42px; font-weight: 600; letter-spacing: 4px;
    text-transform: uppercase; color: var(--brand-blue);
  }
  .brand-rule {
    position: absolute; left: 88px; top: 58px;
    width: 560px; height: 1px; background: var(--rule-grey);
  }
  .brand-tagline {
    position: absolute; left: 88px; top: 66px;
    white-space: nowrap;
    font-size: 14px; font-weight: 500; letter-spacing: 1px;
    color: var(--muted-grey);
  }

  .holder-details {
    position: absolute; right: 505px; top: 290px;
    text-align: right; font-variant: small-caps;
  }
  .holder-name { font-size: 26px; font-weight: 600; color: var(--brand-blue); letter-spacing: 1.5px; }
  .holder-title { font-size: 21px; font-weight: 500; color: var(--text-grey); letter-spacing: 1.5px; margin-top: 4px; }
  .holder-address { font-size: 21px; font-weight: 500; color: var(--text-grey); letter-spacing: 1.5px; margin-top: 38px; line-height: 1.5; }

  .details-divider {
    position: absolute; left: 520px; top: 278px;
    width: 1px; height: 230px; background: var(--rule-grey);
  }

  .contact-list {
    position: absolute; left: 538px; top: 282px; list-style: none;
    font-size: 22px; font-weight: 500; color: var(--text-grey); letter-spacing: 1.5px;
    font-variant: small-caps;
  }
  .contact-item { display: flex; align-items: center; height: 34px; }
  .contact-item.gap-before { margin-top: 22px; }
  .contact-icon { width: 18px; height: 18px; margin-right: 10px; flex: none; }
  .contact-icon circle { fill: var(--icon-grey); }
  .contact-icon path, .contact-icon rect { fill: #fff; }
</style>
</head>
<body>
  <div class="business-card">
    <svg class="card-swoosh" viewBox="0 0 1000 572" aria-hidden="true">
      <path class="swoosh-grey" d="M0,110 Q70,450 390,572 L330,572 Q60,470 0,170 Z"/>
      <path class="swoosh-blue" d="M0,170 Q60,470 330,572 L0,572 Z"/>
    </svg>

    <div class="brand-block">
      <div class="brand-mark"></div>
      <div class="brand-name">Brightwell Holdings</div>
      <div class="brand-rule"></div>
      <div class="brand-tagline">Mind Training | Coaching | Business Development</div>
    </div>

    <div class="holder-details">
      <div class="holder-name">Marcus Hale</div>
      <div class="holder-title">Owner / C.E.O</div>
      <div class="holder-address">Suite # 118, Elm Court,<br>NY 40271</div>
    </div>

    <div class="details-divider"></div>

    <ul class="contact-list">
      <li class="contact-item">
        <svg class="contact-icon" viewBox="0 0 18 18" aria-hidden="true"><circle cx="9" cy="9" r="9"/><path d="M6 4.5l2 2-1 1.2c.6 1.3 1.6 2.3 2.9 2.9l1.2-1 2 2-1.3 1.4C8.8 12.6 5.4 9.2 4.6 6z"/></svg>
        555-210-4837
      </li>
      <li class="contact-item">
        <svg class="contact-icon" viewBox="0 0 18 18" aria-hidden="true"><circle cx="9" cy="9" r="9"/><rect x="6.5" y="4" width="5" height="10" rx="1"/></svg>
        555-318-9264
      </li>
      <li class="contact-item">
        <svg class="contact-icon" viewBox="0 0 18 18" aria-hidden="true"><circle cx="9" cy="9" r="9"/><rect x="5" y="8" width="8" height="5"/><rect x="6.5" y="4.5" width="5" height="3"/></svg>
        555-402-7715
      </li>
      <li class="contact-item gap-before">
        <svg class="contact-icon" viewBox="0 0 18 18" aria-hidden="true"><circle cx="9" cy="9" r="9"/><path d="M4.5 6h9v6h-9z M4.5 6l4.5 3.5 4.5-3.5" /></svg>
        marcus@brightwellhq.com
      </li>
      <li class="contact-item">
        <svg class="contact-icon" viewBox="0 0 18 18" aria-hidden="true"><circle cx="9" cy="9" r="9"/><rect x="4.5" y="8.4" width="9" height="1.2"/><rect x="8.4" y="4.5" width="1.2" height="9"/></svg>
        www.brightwellhq.com
      </li>
    </ul>
  </div>
</body>
</html>
```